BRL business card

For a business card with our logo

Contact Information for Business Card

Mathéo VRANEL
Founder & CEO
email : ceo@brightlanterncollective.com / www.brightlanterncollective.com /
instagram / facebook / WhatsApp
N°: +590 690 482 517

Colors

Designer to choose colors to be used in the design.

```html
<!DOCTYPE html>
<html lang="en">
<head>
<meta charset="utf-8">
<title>BRL business card</title>
<link rel="stylesheet" href="https://fonts.googleapis.com/css2?family=Catamaran:wght@400;500;700&display=swap">
<style>
  :root {
    --brand-blue: #1057a3;
    --brand-orange: #f07427;
    --ink: #1f2933;
    --paper: #ffffff;
    --backdrop: #d9dadc;
  }
  * { margin: 0; padding: 0; box-sizing: border-box; }
  html, body { width: 1200px; height: 960px; overflow: hidden; }
  body {
    background: var(--backdrop);
    font-family: "Catamaran", sans-serif;
    position: relative;
  }
  .card {
    position: absolute;
    left: 265px;
    width: 670px;
    background: var(--paper);
    overflow: hidden;
  }
  .card svg.bands { position: absolute; left: 0; top: 0; }
  .card--front { top: 78px; height: 383px; }
  .card--back { top: 493px; height: 380px; }

  .brand {
    position: absolute;
    display: flex;
    flex-direction: column;
    align-items: center;
    color: var(--brand-blue);
    font-weight: 700;
    text-align: center;
  }
  .brand__dot {
    border-radius: 50%;
    background: var(--brand-orange);
  }
  .card--front .brand { left: 0; width: 670px; top: 94px; }
  .card--front .brand__dot { width: 88px; height: 88px; margin-bottom: 14px; }
  .card--front .brand__name { font-size: 28px; line-height: 1; }

  .card--back .brand { left: 453px; width: 200px; top: 33px; }
  .card--back .brand__dot { width: 50px; height: 50px; margin-bottom: 8px; }
  .card--back .brand__name { font-size: 13px; line-height: 1; }

  .front-web {
    position: absolute;
    left: 0; width: 670px; top: 340px;
    text-align: center;
    color: var(--paper);
    font-size: 17px;
    font-weight: 500;
  }

  .rule {
    position: absolute;
    left: 48px; top: 129px;
    width: 571px; height: 2px;
    background: var(--brand-orange);
  }
  .contacts {
    position: absolute;
    left: 48px; top: 186px;
    list-style: none;
  }
  .contacts li {
    display: flex;
    align-items: center;
    height: 27px;
    font-size: 17px;
    color: var(--ink);
  }
  .contacts svg { width: 18px; height: 18px; margin-right: 12px; fill: var(--brand-blue); }

  .person {
    position: absolute;
    right: 51px; top: 190px;
    text-align: right;
  }
  .person__name { font-size: 29px; line-height: 1; color: var(--ink); font-weight: 400; }
  .person__first { color: var(--brand-blue); font-weight: 700; }
  .person__role { font-size: 18px; color: var(--ink); font-weight: 500; margin-top: 2px; }

  .social {
    position: absolute;
    left: 435px; top: 301px;
    display: flex; gap: 10px;
  }
  .social span {
    width: 24px; height: 24px; border-radius: 50%;
    background: var(--paper);
  }
</style>
</head>
<body>

<section class="card card--front">
  <svg class="bands" width="670" height="383" viewBox="0 0 670 383">
    <rect x="0" y="0" width="670" height="17" fill="var(--brand-blue)"/>
    <rect x="0" y="309" width="670" height="17" fill="var(--brand-orange)"/>
    <path d="M0 286 H238 C264 286 262 326 294 326 H670 V383 H0 Z" fill="var(--brand-blue)"/>
  </svg>
  <div class="brand">
    <div class="brand__dot"></div>
    <div class="brand__name">Bright Lantern Collective</div>
  </div>
  <p class="front-web">www.brightlanterncollective.com</p>
</section>

<section class="card card--back">
  <svg class="bands" width="670" height="380" viewBox="0 0 670 380">
    <rect x="0" y="307" width="670" height="17" fill="var(--brand-orange)"/>
    <path d="M670 286 H452 C424 286 420 324 390 324 H0 V380 H670 Z" fill="var(--brand-blue)"/>
  </svg>
  <div class="brand">
    <div class="brand__dot"></div>
    <div class="brand__name">Bright Lantern Collective</div>
  </div>
  <div class="rule"></div>
  <ul class="contacts">
    <li>
      <svg viewBox="0 0 24 24"><path d="M6.6 10.8a15.5 15.5 0 0 0 6.6 6.6l2.2-2.2a1 1 0 0 1 1-.25 11.4 11.4 0 0 0 3.6.6 1 1 0 0 1 1 1V20a1 1 0 0 1-1 1A17 17 0 0 1 3 4a1 1 0 0 1 1-1h3.5a1 1 0 0 1 1 1c0 1.25.2 2.45.6 3.6a1 1 0 0 1-.25 1Z"/></svg>
      +590 690 482 517
    </li>
    <li>
      <svg viewBox="0 0 24 24"><path d="M2 5h20v14H2Z M3.5 6.5 12 13l8.5-6.5 M3.5 17.5l6-5.5 M20.5 17.5l-6-5.5" fill="none" stroke="var(--brand-blue)" stroke-width="1.8"/></svg>
      ceo@brightlanterncollective.com
    </li>
    <li>
      <svg viewBox="0 0 24 24"><path d="M5 2 L19 14 H12.5 L16 21.5 L13 22.8 L9.6 15.3 L5 19.5 Z"/></svg>
      www.brightlanterncollective.com
    </li>
  </ul>
  <div class="person">
    <h1 class="person__name"><span class="person__first">Mathéo</span> VRANEL</h1>
    <p class="person__role">Founder &amp; CEO</p>
  </div>
  <div class="social" aria-label="Social channels">
    <span></span><span></span><span></span>
  </div>
</section>

</body>
</html>
```